Business card design needed to incorporate existing logo

We need a business card for a new modern Accounting & Business Solutions company call KelvaTrade Services.com.au servicing all of Australia.
My tagline is Steady Ledger Answers... built right.

We specialise in Cloud Accounting and this is our primary focus. We also provide tax representation, debt recovery, computer, tablet and smart phone sales.

I would like a design that uses my corporate, trustworthy colours of blue/white, black/grey however am open to suggestion. I have attached my logo to go on the card somewhere,of which you will see the colour scheme.

I am after a card that STANDS OUT, somewhere between it not being too busy and not being a baron waste of space.

A 'cloud' incorporated in the design may work well, up to your artistic judgement. I know what I like when I see it; it is harder to put into words!

Excited to see your ideas!
I have added my logo predominately (blue/white) and for additional opportunity have added my reverse logo (darker one). I have used the blue/white on my website and letterhead. I will be using both on my vehicle signage.

Target Market(s)

Tradesmen and small-medium businesses of all descriptions Australia-wide

Industry/Entity Type

Debt

Contact Information for Business Card

Dale Pemberton
Principal (optional)
KelvaTrade Services.com.au
Steady Ledger Answers... built right

P: 1800 513 684
M: 0412 860 571 (optional)
W: www.kelvatradeservices.com.au
E: admin@kelvatradeservices.com.au

Logo Text

Steady Ledger Answers... built right!

Logo styles of interest
Wordmark Logo
Requirements
Must have
• Must look professional and of high quality not cheap.

My logo and my tagline 'Steady Ledger Answers... built right'.

I have my colourscheme in mind as per my attached logo, however am open to suggestion. I want to see what you can create that I would not have thought of.

Modern, innovative.
Something I won't look at and think, 'I could have done that myself'.

Must be able to be printed on Norla 300gm premium cards and the artwork provided to me.
Nice to have
• Title of Principal is optional depending on space and judement call of look/fee.
M: (mobile) number is also optional as above.

Somthing cloud related given the Cloud Accounting aspect may be relevant. I leave it to your artistic design and judgement.
Should not have
• Must not look cheap.

```html
<!DOCTYPE html>
<html lang="en">
<head>
<meta charset="utf-8">
<title>KelvaTrade Services – Business Card</title>
<link rel="stylesheet" href="https://fonts.googleapis.com/css2?family=Rye&family=Pinyon+Script&family=Open+Sans:wght@400;600&display=swap">
<style>
  :root {
    --page: #ffffff;
    --navy-deep: #1d2c74;
    --navy: #2b4195;
    --navy-light: #3652a8;
    --sky: #2f8fd6;
    --sky-light: #5cb8ec;
    --cloud-white: #e9f5fb;
    --text-white: #ffffff;
    --text-soft: #cfe4f5;
  }
  * { box-sizing: border-box; margin: 0; padding: 0; }
  html, body {
    width: 1200px;
    height: 693px;
    overflow: hidden;
    background: var(--page);
  }
  .canvas {
    position: relative;
    width: 1200px;
    height: 693px;
  }
  .card {
    position: absolute;
    top: 181px;
    width: 540px;
    height: 330px;
    overflow: hidden;
    background: linear-gradient(160deg, var(--navy-light) 0%, var(--navy) 45%, var(--navy-deep) 100%);
    box-shadow: 0 6px 18px rgba(20, 30, 80, 0.25);
  }
  .card--back { left: 40px; }
  .card--front { left: 620px; }

  /* cloud artwork areas */
  .cloud-art {
    position: absolute;
    background: linear-gradient(180deg, var(--cloud-white) 0%, var(--sky-light) 35%, var(--sky) 100%);
    opacity: 0.9;
  }
  .card--back .cloud-art--bank {
    left: 0; bottom: 0; width: 540px; height: 105px;
    border-radius: 80px 120px 0 0;
  }
  .card--front .cloud-art--top-left {
    left: -20px; top: 12px; width: 230px; height: 80px;
    border-radius: 40px;
  }
  .card--front .cloud-art--right {
    right: -20px; top: 40px; width: 190px; height: 80px;
    border-radius: 40px;
  }
  .card--front .cloud-art--bottom-right {
    right: -10px; bottom: -10px; width: 240px; height: 160px;
    border-radius: 90px 90px 0 0;
  }
  .card--front .cloud-art--small {
    left: 180px; bottom: 22px; width: 110px; height: 46px;
    border-radius: 23px;
  }

  /* back: contact side */
  .holder {
    position: absolute;
    left: 0; right: 0; top: 62px;
    text-align: right;
    padding-right: 100px;
    color: var(--text-white);
  }
  .holder__name {
    font-family: "Rye", serif;
    font-size: 30px;
    letter-spacing: 1px;
    line-height: 1;
  }
  .holder__title {
    font-family: "Pinyon Script", cursive;
    font-size: 28px;
    line-height: 1.1;
    margin-top: 2px;
  }
  .contact {
    position: absolute;
    left: 130px; top: 150px;
    list-style: none;
    color: var(--text-white);
    font-family: "Open Sans", sans-serif;
    font-size: 15px;
    line-height: 1.35;
  }

  /* front: wordmark side */
  .brand {
    position: absolute;
    left: 56px; top: 128px;
    width: 250px;
  }
  .wordmark {
    display: flex;
    align-items: flex-start;
    gap: 12px;
  }
  .wordmark__dot {
    flex: none;
    width: 22px; height: 22px;
    margin-top: 8px;
    border-radius: 50%;
    background: var(--sky-light);
  }
  .wordmark__name {
    font-family: "Open Sans", sans-serif;
    font-weight: 600;
    font-size: 26px;
    line-height: 1.2;
    color: var(--sky-light);
  }
  .brand__tagline {
    margin: 8px 0 0 34px;
    font-family: "Open Sans", sans-serif;
    font-size: 13px;
    color: var(--text-soft);
  }
</style>
</head>
<body>
<main class="canvas">

  <section class="card card--back" aria-label="Business card contact side">
    <div class="cloud-art cloud-art--bank" role="img" aria-label="Stylised blue and white cloud illustration along the bottom"></div>
    <div class="holder">
      <p class="holder__name">Dale Pemberton</p>
      <p class="holder__title">principal</p>
    </div>
    <ul class="contact">
      <li>admin@kelvatradeservices.com.au</li>
      <li>www.kelvatradeservices.com.au</li>
      <li>P: 1800 513 684</li>
    </ul>
  </section>

  <section class="card card--front" aria-label="Business card logo side">
    <div class="cloud-art cloud-art--top-left" role="img" aria-label="Stylised cloud illustration, top left"></div>
    <div class="cloud-art cloud-art--right" role="img" aria-label="Stylised cloud illustration, right"></div>
    <div class="cloud-art cloud-art--bottom-right" role="img" aria-label="Large stylised cloud illustration, bottom right"></div>
    <div class="cloud-art cloud-art--small" role="img" aria-label="Small stylised cloud illustration"></div>
    <div class="brand">
      <div class="wordmark">
        <span class="wordmark__dot"></span>
        <span class="wordmark__name">KelvaTrade Services.com.au</span>
      </div>
      <p class="brand__tagline">Steady Ledger Answers... built right</p>
    </div>
  </section>

</main>
</body>
</html>
```